Website Graphic Layout

We are looking for someone to provide a crisp clean layout for our new website design.
The site is runs on Drupal & we like the 4 column layout
We think that the current site is a bit cluttered & could be a bit cleaner.

http://www.tovaquen.org/volunteer-abroad

We like the following website as examples as they are quite clean with a large header image & sub areas to add things such as news testimonials etc

http://brastik.com/
http://www.quorvan.com/ie/
http://lantrevoda.org/
http://www.kelvasp.com/

```html
<!DOCTYPE html>
<html lang="en">
<head>
<meta charset="utf-8">
<title>OVA Intercultural Learning</title>
<link href="https://fonts.googleapis.com/css2?family=Arimo:wght@400;700&family=Open+Sans:wght@400;600&display=swap" rel="stylesheet">
<style>
:root{
  --green-dark:#006b32;
  --green:#00a04a;
  --green-mid:#0a8a3e;
  --green-light:#9ddfa8;
  --orange:#f7941d;
  --blue:#0a4ee0;
  --blue-light:#1f7cf5;
  --footer:#e2e2e2;
  --link:#3aaa35;
  --white:#fff;
  --ink:#222;
}
*{margin:0;padding:0;box-sizing:border-box}
html,body{width:1200px;height:1006px;overflow:hidden;background:var(--white)}
body{position:relative;font-family:Arimo,Arial,sans-serif}
.abs{position:absolute}
.header-band{left:0;top:0;width:1200px;height:75px;background:linear-gradient(180deg,#b8ecc0 0%,var(--green-light) 60%,#7dd08d 100%);box-shadow:0 3px 4px rgba(0,0,0,.25)}
.logo-area{left:247px;top:0;width:380px;height:75px}
.logo{left:278px;top:14px;font-size:44px;color:var(--green-dark);font-family:Arimo,sans-serif;letter-spacing:-1px}
.social{left:630px;top:2px;display:flex;gap:10px}
.social span{width:24px;height:24px;border-radius:50%;background:#2f8fd6;border:2px solid #fff}
.welcome{left:634px;top:29px;color:var(--white);font-weight:700;font-size:14px;line-height:14px;white-space:nowrap}
.call-label{left:823px;top:4px;color:var(--orange);font-weight:700;font-size:23px}
.call-nums{left:823px;top:32px;color:var(--white);font-weight:700;font-size:19px;line-height:20px}
.phone-icon{left:782px;top:8px}
.main-nav{left:246px;top:86px;width:686px;height:30px;background:linear-gradient(180deg,#10b656,var(--green-mid));border-radius:3px;box-shadow:0 2px 3px rgba(0,0,0,.35);display:flex}
.main-nav a{color:var(--white);font-weight:700;font-size:11.5px;text-decoration:none;display:flex;align-items:center;justify-content:center;border-right:2px solid #0c6f33;height:100%;white-space:nowrap}
.main-nav a:last-child{border:none}
.hero{left:250px;top:126px;width:438px;height:234px;background:linear-gradient(135deg,#6b5a4a,#b58f7a 40%,#6e8a77 70%,#3c4f3b)}
.hero-curve{left:248px;top:118px}
.news-overlay{left:430px;top:178px;width:238px;height:186px;background:rgba(255,255,255,.3);border-radius:4px}
.news-word{left:498px;top:248px;color:rgba(255,255,255,.8);font-size:31px;font-weight:700}
.news-tag{left:250px;top:314px;width:158px;height:34px;background:rgba(255,255,255,.85);color:var(--orange);font-weight:700;font-size:12px;padding:10px 0 0 30px;white-space:nowrap}
.sub-nav{left:250px;top:370px;width:433px;height:38px;background:var(--green);border-radius:3px;box-shadow:0 2px 3px rgba(0,0,0,.3);display:flex}
.sub-nav a{color:var(--white);font-weight:700;font-size:14px;text-decoration:none;text-align:center;padding-top:6px;border-right:2px solid #0c6f33;height:100%;white-space:nowrap}
.sub-nav a:last-child{border:none}
.finder{left:709px;top:130px;width:222px;height:273px;background:var(--green-dark);border-radius:3px;overflow:hidden}
.finder-top{left:0;top:0;width:222px;height:62px;background:linear-gradient(180deg,#0a9a45,#06803a)}
.finder-title{left:94px;top:14px;color:var(--white);font-family:'Open Sans',sans-serif;font-size:19px;line-height:16px}
.field{width:164px;height:17px;background:var(--white);border-radius:8px;font-size:9px;font-weight:700;color:var(--ink);padding:3px 0 0 18px}
.search-btn{left:132px;top:244px;width:85px;height:17px;background:var(--white);border-radius:7px;font-size:9px;font-weight:700;text-align:center;padding-top:3px}
.featured{left:245px;top:426px;width:690px;height:164px;background:linear-gradient(180deg,var(--green-mid),var(--green-dark));border-radius:3px}
.tab{top:14px;color:var(--white);font-size:11px;font-weight:700;white-space:nowrap}
.photo{top:80px;color:var(--white);font-family:'Open Sans',sans-serif;font-size:16px}
.arrow-btn{top:72px;width:34px;height:34px;border-radius:50%;background:var(--orange)}
.view{top:150px;width:47px;height:16px;background:var(--orange);font-size:9px;font-weight:700;text-align:center;padding-top:3px;color:var(--ink)}
.promo{top:619px;height:77px;background:linear-gradient(180deg,var(--blue-light),var(--blue));border-radius:3px;color:var(--white);font-family:'Open Sans',sans-serif;font-size:15px;line-height:15px;letter-spacing:-.2px;white-space:nowrap}
.footer{left:0;top:730px;width:1200px;height:276px;background:var(--footer);border-top:2px solid var(--link)}
.links-title{left:272px;top:764px;color:var(--link);font-family:'Open Sans',sans-serif;font-size:19px}
.link-col{top:796px;display:flex;flex-direction:column;gap:11px;color:var(--link);font-family:'Open Sans',sans-serif;font-size:14px;line-height:19px;white-space:nowrap}
.divider{left:0;top:932px;width:1200px;height:1px;background:#a5a5a5}
.address{left:253px;top:946px;font-size:10.5px;line-height:15px;color:var(--ink);white-space:nowrap}
.footer-logo{left:824px;top:942px;color:var(--green);font-weight:700;font-size:38px}
</style>
</head>
<body>
<header>
  <div class="abs header-band"></div>
  <svg class="abs logo-area" width="380" height="75" viewBox="0 0 380 75" aria-hidden="true">
    <path d="M0 0 H265 Q345 20 372 75 H0 Z" fill="#fff"/>
    <path d="M110 0 Q300 0 375 75 L366 75 Q290 10 110 3 Z" fill="#2bb24c"/>
  </svg>
  <div class="abs logo">LOGO</div>
  <div class="abs social" aria-label="Social links"><span></span><span></span><span></span><span></span></div>
  <div class="abs welcome">WELCOME GUEST.<br>LOGIN. REGISTER.<br>CONTACT US.</div>
  <svg class="abs phone-icon" width="34" height="78" viewBox="0 0 34 78" aria-hidden="true">
    <path d="M22 4 C8 6 4 22 6 40 C8 58 16 72 26 72 L30 62 L22 56 L18 60 C14 52 13 34 16 24 L22 24 L26 14 Z" fill="#2a2a2a"/>
  </svg>
  <div class="abs call-label">CALL US</div>
  <div class="abs call-nums">1850 604817<br>&nbsp;021 7730264</div>
  <nav class="abs main-nav">
    <a style="width:67px">HOME</a>
    <a style="width:127px">STUDY ABROAD</a>
    <a style="width:166px">VOLUNTEER ABROAD</a>
    <a style="width:208px">DEVELOPMENT EDUCATION</a>
    <a style="width:118px">TRAVEL AWARDS</a>
  </nav>
</header>

<main>
  <div class="abs hero" role="img" aria-label="Group photo of volunteers and local children"></div>
  <svg class="abs hero-curve" width="442" height="250" viewBox="0 0 442 250" aria-hidden="true">
    <path d="M0 8 Q220 0 442 4 L442 10 Q220 4 2 12 Z" fill="#1aa34a"/>
    <path d="M2 242 Q220 250 442 240 L442 246 Q220 254 0 246 Z" fill="#1aa34a"/>
  </svg>
  <div class="abs news-overlay"></div>
  <div class="abs news-word">NEWS</div>
  <div class="abs news-tag">NEWS AND EVENT →</div>
  <nav class="abs sub-nav">
    <a style="width:163px">VISIT IRELAND</a>
    <a style="width:101px">ABOUT OVA</a>
    <a style="width:169px;text-align:left;padding-left:20px">COMMUNITY</a>
  </nav>

  <section class="abs finder">
    <div class="abs finder-top"></div>
    <svg class="abs" style="left:4px;top:0" width="86" height="62" viewBox="0 0 86 62" aria-hidden="true">
      <path d="M22 0 H62 V20 H84 L42 60 L0 20 H22 Z" fill="#8ed11f"/>
    </svg>
    <div class="abs finder-title">FIND YOUR<br>PROJECT</div>
    <div class="abs field" style="left:7px;top:106px">REGION...</div>
    <div class="abs field" style="left:7px;top:154px">PROJECT TYPE...</div>
    <div class="abs field" style="left:7px;top:197px">DURATION...</div>
    <div class="abs search-btn">SEARCH...</div>
  </section>

  <section class="abs featured">
    <div class="abs tab" style="left:18px">→ &nbsp; FEATURED PROGRAMME</div>
    <div class="abs tab" style="left:198px">→ &nbsp; NEWS AND EVENTS</div>
    <div class="abs tab" style="left:388px">→ &nbsp; TESTIMONIALS</div>
    <div class="abs tab" style="left:556px">→ &nbsp; FEATURED VIDEOS</div>
    <svg class="abs arrow-btn" style="left:15px" viewBox="0 0 34 34" aria-hidden="true"><path d="M20 9 L12 17 L20 25" stroke="#fff" stroke-width="2" fill="none"/></svg>
    <svg class="abs arrow-btn" style="left:652px" viewBox="0 0 34 34" aria-hidden="true"><path d="M14 9 L22 17 L14 25" stroke="#fff" stroke-width="2" fill="none"/></svg>
    <div class="abs photo" style="left:66px">PHOTO</div>
    <div class="abs photo" style="left:242px">PHOTO</div>
    <div class="abs photo" style="left:423px">PHOTO</div>
    <div class="abs photo" style="left:582px">PHOTO</div>
    <div class="abs view" style="left:137px">VIEW →</div>
    <div class="abs view" style="left:325px">VIEW →</div>
    <div class="abs view" style="left:485px">VIEW →</div>
    <div class="abs view" style="left:645px">VIEW →</div>
  </section>

  <div class="abs promo" style="left:245px;width:229px;padding:9px 9px">Discover our 5 most popular<br>destinations:&nbsp; Vietnam, India,<br>Guatemala, Thailand and<br>Ghana</div>
  <div class="abs promo" style="left:488px;width:200px;text-align:center;padding-top:7px">TALK TO US<br><span style="display:block;margin-top:6px;font-size:16px">Call 021 7 73 02 64<br>Lo-Call 1850 60 48 17</span></div>
  <div class="abs promo" style="left:704px;width:230px;padding:12px 24px">Watch our new VIDEO<br>to find out more about<br>OVA Intercultural Learning</div>
</main>

<footer>
  <div class="abs footer"></div>
  <div class="abs links-title">LINKS</div>
  <div class="abs link-col" style="left:263px"><span>Countries &nbsp;⟶</span><span>Fin your project</span><span>Under 18- programme</span><span>Internship programme</span></div>
  <div class="abs link-col" style="left:425px"><span>Corporate Volunting &nbsp;⟶</span><span>School Programme</span><span>Fundraising</span><span>News</span></div>
  <div class="abs link-col" style="left:608px"><span>Why OVA? &nbsp;&nbsp;⟶</span><span>Is this for me?</span><span>Why Pay?</span><span>How do i apply?</span></div>
  <div class="abs link-col" style="left:784px"><span>FAQ</span><span>About us</span><span>Contact us</span></div>
  <div class="abs divider"></div>
  <div class="abs address">OVA Intercultural Learning, 14 Harbour Row, Lisnagar North, Cork, County Cork, Republic of Ireland.<br>email: info@ovalearning.org telephone: +353 (0)21 7730264 lowcall: 1850 604817 fax: +353 (0)21 7730288<br>cc by-sa 2013 OVA Intercultural Learning</div>
  <div class="abs footer-logo">LOGO</div>
</footer>
</body>
</html>
```